Poster - Series of Poster Designs

We have a number of motivational quotes related to weight loss and fitness which need putting into a series of posters.
The designs need to:
- Reflect the current brand (see www.bluefernhaven.com.au)
- Be designed with scalability in mind to fit to A1, A3, A4, and A5. All portrait layout.
- Incorporate our logo
- Any images need to relfect the diversity of our clients ranging from 70kgs up to 200kgs.
- We have a stock of photos which can be used, or you can source your own (subject to budget approval)
Total of 26 posters in total, but all on the same design series (so effectively 1 design, with 26 applications).
The series of quotes are attached. An example quote would be:
-
"The difference between your body this week and next week is what you do for the next seven days to achieve your goals"
-
Our clients are a range of ages (20 - 60) and split male/female so colours should be neutral and reflect our orange/green branding. A modern feel but not super modern.
Output needs to be A3 ready to print with all source files included so that we can amend in the future.
There may be ongoing work for the right designer.

```html
<!DOCTYPE html>
<html lang="en">
<head>
<meta charset="utf-8">
<title>Bluefern Weight Loss Retreat – Motivational Poster</title>
<link rel="stylesheet" href="https://fonts.googleapis.com/css2?family=Anton&display=swap">
<style>
  :root {
    --bg: #000000;
    --brand-green: #7cc242;
    --brand-orange: #f7941d;
    --pale-green: #dcefc4;
    --light-green: #b5dc8a;
    --white: #ffffff;
    --grey-text: #bdbdbd;
    --yellow: #f3e600;
    --figure-dark: #3a3a3a;
    --figure-light: #a9a9a9;
  }
  * { margin: 0; padding: 0; box-sizing: border-box; }
  html, body {
    width: 849px;
    height: 1200px;
    overflow: hidden;
    background: var(--bg);
  }
  .poster {
    position: relative;
    width: 849px;
    height: 1200px;
    background: var(--bg);
    font-family: "Anton", "Impact", sans-serif;
    text-transform: uppercase;
    color: var(--white);
  }

  /* Brand name */
  .brand {
    position: absolute;
    top: 30px;
    right: 30px;
    display: flex;
    align-items: baseline;
    gap: 16px;
  }
  .brand-name {
    font-size: 44px;
    line-height: 48px;
    color: var(--white);
    letter-spacing: 1px;
  }
  .brand-tagline {
    font-size: 18px;
    line-height: 20px;
    color: var(--grey-text);
    letter-spacing: 1.5px;
  }

  /* Illustration area */
  .journey-art {
    position: absolute;
    top: 112px;
    left: 34px;
    width: 790px;
    height: 622px;
    background: linear-gradient(90deg, var(--figure-dark) 0%, #6e6e6e 55%, var(--figure-light) 80%, #d8d8d8 100%);
    opacity: 0.85;
  }

  /* Quote */
  .quote {
    position: absolute;
    top: 742px;
    left: 30px;
    width: 792px;
  }
  .line { display: block; white-space: nowrap; }
  .line-lead {
    font-size: 56px;
    line-height: 62px;
    color: var(--pale-green);
    letter-spacing: 0.4px;
  }
  .line-split {
    display: flex;
    align-items: center;
    justify-content: space-between;
    margin-top: 6px;
  }
  .line-week {
    font-size: 54px;
    line-height: 58px;
    color: var(--brand-green);
  }
  .line-days {
    font-size: 30px;
    line-height: 31px;
    color: var(--light-green);
    text-align: right;
    letter-spacing: 0.5px;
  }
  .line-mind-game {
    font-size: 64px;
    line-height: 68px;
    color: var(--brand-orange);
    margin-top: 6px;
  }
  .line-change {
    font-size: 49px;
    line-height: 56px;
    color: var(--white);
    margin-top: 12px;
    word-spacing: 10px;
  }
  .accent {
    color: var(--brand-orange);
    border-bottom: 3px solid var(--brand-orange);
  }
  .line-start {
    font-size: 51px;
    line-height: 52px;
    color: var(--yellow);
    margin-top: 10px;
  }
</style>
</head>
<body>
<main class="poster">
  <header class="brand">
    <span class="brand-name">BLUEFERN</span>
    <span class="brand-tagline">Weight Loss Retreat</span>
  </header>

  <div class="journey-art" role="img" aria-label="Row of grey silhouettes of people, from larger figures on the left to slimmer figures on the right, ending with a white silhouette leaping joyfully"></div>

  <section class="quote">
    <span class="line line-lead">The difference between your body</span>
    <div class="line-split">
      <span class="line line-week">This week &amp; next week</span>
      <span class="line-days">Is what you do for<br>the next 7 days</span>
    </div>
    <span class="line line-mind-game">Loosing weight is a mind game</span>
    <span class="line line-change">Change your <span class="accent">mind</span> change your <span class="accent">body</span></span>
    <span class="line line-start">You don't have to be great to start,<br>but you have to start to be great</span>
  </section>
</main>
</body>
</html>
```